Sign for our backyard barnyard

Want a sign to be printed/painted on a 2'x4' board for my wife's backyard barnyard.
Updates

Reason: This is the only extension I can offer to complete the project on time. Thank you for the submissions received so far.

Reason: We are so close to final selection!

Target Market(s)

Our friends who come to visit the barnyard! This is a birthday present for my wife who takes care of the animals.

Font styles to use
Other font styles liked:
• A font that gives the image of a rural farm setting.

Requirements
Must have
• Barnyard is called Quiet Willow Glen. Should have a "farm style" letter treatment of that name as a logo element. Each of the 3 words should have a theme component, don't have to be obvious (like a big smile for happy) but should be worked subtly into design. Current animals in barnyard include chickens, goats and a potbelly pig so animal imagery or silhouette for those is good. Classic "Barn Red" is a good background or theme color for the design. Sign should be horizontally oriented. Needs to be printed on something that holds up outside but can be on plastic that mounts to wood.

```html
<!DOCTYPE html>
<html lang="en">
<head>
<meta charset="utf-8">
<title>Quiet Willow Glen – Barnyard Sign</title>
<link rel="stylesheet" href="https://fonts.googleapis.com/css2?family=Rye&display=swap">
<style>
  :root {
    --barn-red: #c10610;
    --barn-red-deep: #8f0008;
    --barn-red-light: #d4121b;
    --plank-seam: #5e0005;
    --tin-light: #f2f2f2;
    --tin-mid: #d6d6d6;
    --tin-dark: #a9a9a9;
    --letter-white: #ffffff;
    --letter-grey: #c9c9c9;
    --silhouette: #e4e4e4;
  }

  html, body {
    margin: 0;
    padding: 0;
    width: 1200px;
    height: 600px;
    overflow: hidden;
    background: var(--barn-red);
  }

  .sign {
    position: relative;
    width: 1200px;
    height: 600px;
    overflow: hidden;
    background:
      radial-gradient(ellipse at 50% 45%, var(--barn-red-light) 0%, var(--barn-red) 55%, var(--barn-red-deep) 100%);
  }

  .tin-cap {
    position: absolute;
    left: 0;
    top: 0;
    width: 1200px;
    height: 52px;
    background: linear-gradient(180deg, var(--tin-light) 0%, var(--tin-mid) 70%, var(--tin-dark) 100%);
    box-shadow: 0 3px 6px rgba(0, 0, 0, 0.45);
    z-index: 2;
  }

  .planks {
    position: absolute;
    inset: 0;
    z-index: 1;
  }

  .plank-seam {
    stroke: var(--plank-seam);
    stroke-width: 3;
    opacity: 0.8;
  }

  .farm-name {
    position: absolute;
    left: 0;
    top: 0;
    width: 1200px;
    height: 600px;
    z-index: 4;
  }

  .farm-name text {
    font-family: "Rye", "Georgia", serif;
    fill: url(#letter-fill);
    filter: url(#letter-drop);
  }

  .animal-silhouettes {
    position: absolute;
    left: 252px;
    top: 446px;
    width: 620px;
    height: 136px;
    z-index: 3;
    border-radius: 36px 52px 12px 12px;
    background: linear-gradient(180deg, var(--letter-white) 0%, var(--silhouette) 100%);
    opacity: 0.9;
  }
</style>
</head>
<body>
  <main class="sign">
    <div class="tin-cap"></div>

    <svg class="planks" width="1200" height="600" viewBox="0 0 1200 600" aria-hidden="true">
      <line class="plank-seam" x1="0" y1="176" x2="1200" y2="172"/>
      <line class="plank-seam" x1="0" y1="296" x2="1200" y2="292"/>
      <line class="plank-seam" x1="0" y1="416" x2="1200" y2="413"/>
      <line class="plank-seam" x1="0" y1="540" x2="1200" y2="536"/>
    </svg>

    <svg class="farm-name" width="1200" height="600" viewBox="0 0 1200 600">
      <defs>
        <linearGradient id="letter-fill" x1="0" y1="0" x2="0" y2="1">
          <stop offset="0%" stop-color="#ffffff"/>
          <stop offset="65%" stop-color="#f2f2f2"/>
          <stop offset="100%" stop-color="#c9c9c9"/>
        </linearGradient>
        <filter id="letter-drop" x="-10%" y="-10%" width="120%" height="130%">
          <feDropShadow dx="-6" dy="8" stdDeviation="5" flood-color="#280000" flood-opacity="0.6"/>
        </filter>
      </defs>
      <title>Quiet Willow Glen</title>
      <text class="name-top" x="600" y="248" text-anchor="middle" font-size="200"
            textLength="660" lengthAdjust="spacingAndGlyphs">QUIET</text>
      <text class="name-bottom" x="602" y="410" text-anchor="middle" font-size="165"
            textLength="965" lengthAdjust="spacingAndGlyphs">WILLOW GLEN</text>
    </svg>

    <div class="animal-silhouettes" role="img"
         aria-label="White distressed silhouettes of a potbelly pig, a goat and a chicken standing in a row"></div>
  </main>
</body>
</html>
```